Online plant nursery needs3 seperate slides for a intro web site slide slide show

We need 3 slide graphics / banners measurments should be 960wide 540 tall and 2mb or smaller. We are an online mail order nursery that focuses sales on Peonies.
Slide 1: Use faded out photos of Peony Garden with many flowers just budding. Our logo and the Words "A Lost Spring is Never Found Again". try to use our logo in a small small watermark on all slides.
Slide 2: Use your own creativity for the slide.... message should say "Free Shipping"
Slide 3: Use your own creativity for the slide .... messgae "Shop Our Other Items". To see site it will be used on go to http://k4830157.tbrwxq9pnlhe.preview82.shopnestle-example.com/

Target Market(s)

home owners age 30 - 65.

Industry/Entity Type

Nursery

Requirements
Must have
• must transition well.
Should not have
• can not be larger than 2MB per file

```html
<!DOCTYPE html>
<html lang="en">
<head>
<meta charset="utf-8">
<title>Free Shipping</title>
<link rel="stylesheet" href="https://fonts.googleapis.com/css2?family=Kaushan+Script&display=swap">
<style>
  :root {
    --violet-light: #b565dc;
    --violet-mid: #8e2fc4;
    --violet-deep: #5a1a8c;
    --violet-night: #3a0f63;
    --ink-white: #ffffff;
  }
  html, body {
    margin: 0;
    padding: 0;
    width: 1200px;
    height: 675px;
    overflow: hidden;
    background: var(--violet-mid);
  }
  .slide {
    position: relative;
    width: 1200px;
    height: 675px;
    overflow: hidden;
  }
  .slide__backdrop {
    position: absolute;
    inset: 0;
    background:
      radial-gradient(circle at 92% 22%, var(--violet-night) 0%, rgba(58, 15, 99, 0.75) 18%, rgba(90, 26, 140, 0) 42%),
      radial-gradient(circle at 18% 78%, var(--violet-night) 0%, rgba(58, 15, 99, 0.7) 20%, rgba(90, 26, 140, 0) 44%),
      radial-gradient(ellipse at 55% 40%, var(--violet-light) 0%, rgba(181, 101, 220, 0.4) 30%, rgba(181, 101, 220, 0) 60%),
      linear-gradient(160deg, var(--violet-mid) 0%, var(--violet-light) 50%, var(--violet-mid) 100%);
  }
  .slide__frame {
    position: absolute;
    left: 61px;
    top: 97px;
    width: 1079px;
    height: 481px;
    border: 2px solid var(--ink-white);
    box-sizing: border-box;
  }
  .slide__headline {
    position: absolute;
    left: 0;
    right: 0;
    top: 230px;
    margin: 0;
    padding-right: 45px;
    text-align: center;
    font-family: "Kaushan Script", cursive;
    font-weight: 400;
    font-size: 140px;
    line-height: 1.2;
    color: var(--ink-white);
    letter-spacing: 2px;
  }
</style>
</head>
<body>
  <main class="slide">
    <div class="slide__backdrop" role="img" aria-label="Abstract pattern of overlapping translucent purple circles, darker at the upper right and lower left"></div>
    <div class="slide__frame"></div>
    <h1 class="slide__headline">Free Shipping</h1>
  </main>
</body>
</html>
```